Pebblo Bites - Product Packaging (Snack wrapper)

Pebblo Bites is looking for our next package design! Our snack products are all-natural, gluten-free, vegan, and paleo. Our mission is to bring clean, wholesome snacks back into the market. The package design is for our individual wrappers that hold two of our snack bites.

The background will be matte white with a transparent window integrated so that customers can see the bites inside.

The final design will be clean and modern, using white as the background, black for text, and our logos yellow. We have multiple different flavors, so each flavor will have its own unique color accents that must be editable in the final file. The accent colors should be bold and take up an equal amount of space as the white does.

The packaging will stand out on a busy shelf and entice customers as an easy on-the-go, wholesome snack. The back of the package must have a space for a nutrition box and ingredients list. Our logo is attached. The logo graphic can be separated (it doesnt have to stay in the same layout you see). We have attached an example of our old product label, too.

The package dimensions are 4inches wide x 5 inches long with a 1/2inch of the length at the top and 1/2inch of the length at the bottom being blank for sealing. Thank you!

Target Market(s)

Cafe goers, health-conscience, kids, active.

Font styles to use
Sans Serif

Colors
fbed22
ffffff
000000

Requirements
Must have
• Must show that our product is gluten-free, vegan, and paleo. Must have editable flavor name, and flavor accent colors for our multiple different flavors. Must use our logo and company yellow.

```html
<!DOCTYPE html>
<html lang="en">
<head>
<meta charset="utf-8">
<title>Pebblo Bites – Chocolate Chip Wrapper</title>
<link rel="stylesheet" href="https://fonts.googleapis.com/css2?family=Amatic+SC:wght@700&family=Roboto+Condensed:wght@400;700&family=Arimo:wght@700&display=swap">
<style>
  :root {
    --stage: #202020;
    --wrapper: #fafafa;
    --ink: #111111;
    --brand-yellow: #f8de6a;
    --seal-line: #555555;
    --cookie-light: #a8765a;
    --cookie-dark: #6b4030;
    --badge: #fdfdfd;
  }
  * { margin: 0; padding: 0; box-sizing: border-box; }
  html, body {
    width: 1200px;
    height: 800px;
    overflow: hidden;
    background: var(--stage);
  }
  .wrapper-front {
    position: absolute;
    left: 312px;
    top: 40px;
    width: 576px;
    height: 720px;
    background: var(--wrapper);
    overflow: hidden;
  }
  .seal-line {
    position: absolute;
    left: 0;
    width: 100%;
    border-top: 1.5px dashed var(--seal-line);
  }
  .seal-line--top { top: 70px; }
  .seal-line--bottom { top: 650px; }
  .brand-name {
    position: absolute;
    top: 82px;
    left: 0;
    width: 100%;
    text-align: center;
    font-family: "Roboto Condensed", sans-serif;
    font-weight: 700;
    font-size: 62px;
    line-height: 1;
    color: var(--brand-yellow);
  }
  .hero,
  .product-title {
    position: absolute;
    left: 0;
    top: 0;
    width: 576px;
    height: 720px;
    overflow: visible;
  }
  .product-title text {
    font-family: "Amatic SC", sans-serif;
    font-weight: 700;
    font-size: 94px;
    fill: var(--ink);
  }
  .flavor-name {
    position: absolute;
    top: 566px;
    left: 0;
    width: 576px;
    text-align: center;
    font-family: "Roboto Condensed", sans-serif;
    font-weight: 400;
    font-size: 40px;
    line-height: 1;
    color: var(--ink);
  }
  .flavor-rule {
    position: absolute;
    top: 611px;
    left: 141px;
    width: 292px;
    border-top: 1.5px solid var(--ink);
  }
  .diet-claims {
    position: absolute;
    top: 617px;
    left: 0;
    width: 576px;
    text-align: center;
    font-family: "Arimo", sans-serif;
    font-weight: 700;
    font-size: 19px;
    line-height: 1.2;
    color: var(--brand-yellow);
    word-spacing: 2px;
  }
  .diet-claims .dot { margin: 0 10px; }
</style>
</head>
<body>
  <main class="wrapper-front">
    <div class="seal-line seal-line--top"></div>
    <div class="seal-line seal-line--bottom"></div>

    <div class="brand-name">Pebblo</div>

    <svg class="hero" viewBox="0 0 576 720">
      <defs>
        <radialGradient id="cookie-tone" cx="45%" cy="45%" r="60%">
          <stop offset="0%" stop-color="#a8765a"/>
          <stop offset="100%" stop-color="#6b4030"/>
        </radialGradient>
      </defs>
      <circle class="cookie-window" cx="283" cy="413" r="142" fill="url(#cookie-tone)"
              role="img" aria-label="Photo of a chocolate chip cookie seen through the window"/>
      <circle class="brand-badge" cx="368" cy="317" r="89" fill="#fdfdfd"/>
    </svg>

    <svg class="product-title" viewBox="0 0 576 720">
      <defs>
        <path id="title-arc" d="M 40 262 Q 290 222 540 276" fill="none"/>
      </defs>
      <text text-anchor="middle"><textPath href="#title-arc" startOffset="50%">COOKIE BITES</textPath></text>
    </svg>

    <div class="flavor-name">Chocolate Chip</div>
    <div class="flavor-rule"></div>
    <div class="diet-claims">Gluten-free<span class="dot">•</span>Vegan<span class="dot">•</span>Paleo</div>
  </main>
</body>
</html>
```